Marcus Bellamy & Golden Lanterns

I need a cd cover designed for a Gospel/Christian Choir. I'm attaching the main picture I want on the cover. This is our single "Hold on through morning".

Requirements
Must have
• Single name: Hold On Through Morning

```html
<!DOCTYPE html>
<html lang="en">
<head>
<meta charset="UTF-8">
<title>Hold On Through Morning — Single Cover</title>
<link href="https://fonts.googleapis.com/css2?family=Bree+Serif&family=Montserrat:wght@500&display=swap" rel="stylesheet">
<style>
  :root {
    --bg: #ffffff;
    --night: #14121c;
    --navy: #1d2233;
    --brick: #c8662a;
    --brick-dark: #6e3318;
    --lamp: #ffd27a;
    --title-face: #f3cfc3;
    --title-depth: #a8316b;
    --title-deep: #5e1238;
    --url: #f4efe9;
  }
  * { margin: 0; padding: 0; box-sizing: border-box; }
  html, body {
    width: 1200px;
    height: 923px;
    overflow: hidden;
    background: var(--bg);
  }
  .canvas {
    position: relative;
    width: 1200px;
    height: 923px;
    display: flex;
    align-items: center;
    justify-content: center;
  }
  .cover {
    position: relative;
    width: 660px;
    height: 634px;
    overflow: hidden;
  }
  .cover-photo {
    position: absolute;
    inset: 0;
    background:
      radial-gradient(circle at 10% 8%, var(--lamp) 0, rgba(255,200,110,0.55) 6%, rgba(255,160,70,0) 22%),
      radial-gradient(ellipse at 70% 20%, rgba(225,120,55,0.95) 0, rgba(200,102,42,0.7) 30%, rgba(110,51,24,0) 65%),
      linear-gradient(90deg, var(--night) 0%, #2a1d1a 30%, var(--brick-dark) 60%, var(--brick) 100%);
  }
  .cover-photo::after {
    content: "";
    position: absolute;
    inset: 0;
    background: linear-gradient(180deg, rgba(20,18,28,0) 45%, rgba(29,34,51,0.85) 100%);
  }
  .site-url {
    position: absolute;
    top: 30px;
    left: 0;
    right: 0;
    text-align: center;
    font-family: "Montserrat", sans-serif;
    font-weight: 500;
    font-size: 11px;
    letter-spacing: 0.45em;
    color: var(--url);
  }
  .single-title {
    position: absolute;
    left: 170px;
    top: 300px;
    width: 460px;
    font-family: "Bree Serif", serif;
    color: var(--title-face);
    line-height: 0.95;
    text-shadow:
      1px 2px 0 var(--title-depth),
      2px 4px 0 var(--title-depth),
      3px 6px 0 var(--title-depth),
      4px 8px 0 var(--title-deep),
      6px 12px 10px rgba(0,0,0,0.45);
  }
  .single-title span { display: block; }
  .title-line-1 { font-size: 74px; }
  .title-line-2 { font-size: 48px; padding-left: 120px; }
  .title-line-3 { font-size: 74px; }
</style>
</head>
<body>
  <main class="canvas">
    <section class="cover">
      <div class="cover-photo" role="img" aria-label="Night street photo of the choir leader in a dark suit seated at a piano beside a lit lamp post and brick wall"></div>
      <p class="site-url">WWW.goldenlanterns.COM</p>
      <h1 class="single-title">
        <span class="title-line-1">Hold On</span>
        <span class="title-line-2">Through</span>
        <span class="title-line-3">Morning</span>
      </h1>
    </section>
  </main>
</body>
</html>
```